Plumbing company needs Business Card Design

Hi I need business card design based on logo which I uploaded. Its plumbing and heating company called Wodorex Usługi Hydrauliczno-Gazowe. I want to see on my card motto of my company which is "...od wymiany uszczelki po wymiane łazienki.", my phone number, name, and website: 608472915, Marek Kowalczyk, info@wodorex-example.org, www.wodorex-example.org
I want to see logos of companys which I'm approved installer (Termovo) (Le Varnoux) (Kelm) (Ostra).
I want new creative look of business card. I like rounded corners.
Any questions please send message.
Thanks for intrest.
Industry/Entity Type
Business
Contact Information for Business Card
Marek Kowalczyk
608 472 915
info@wodorex-example.org
www.wodorex-example.org
...od wymiany uszczelki po wymiane łazienki.

```html
<!DOCTYPE html>
<html lang="pl">
<head>
<meta charset="utf-8">
<title>Wodorex – wizytówka</title>
<link href="https://fonts.googleapis.com/css2?family=Quicksand:wght@500;700&display=swap" rel="stylesheet">
<style>
  :root{
    --bg:#e4e4e2;
    --paper:#f4f4f4;
    --red:#d8262b;
    --navy:#2c4a93;
    --navy-deep:#23397a;
    --yellow:#f2ea2a;
    --ink:#1f2a44;
    --white:#ffffff;
  }
  *{box-sizing:border-box;margin:0;padding:0}
  html,body{width:1200px;height:1000px;overflow:hidden;background:var(--bg);font-family:"Quicksand",sans-serif}
  .sheet{position:relative;width:1200px;height:1000px}
  .card{position:absolute;left:210px;width:780px;height:446px;border-radius:18px;overflow:hidden;background:var(--paper);box-shadow:0 6px 18px rgba(0,0,0,.18)}
  .card--front{top:36px}
  .card--back{top:518px}
  .card svg.shapes{position:absolute;inset:0;width:100%;height:100%}

  .brand{position:absolute;display:flex;align-items:center;gap:12px;color:var(--navy);font-weight:700}
  .brand__mark{width:54px;height:54px;background:var(--yellow);border-radius:8px;flex:none}
  .brand__name{font-size:44px;line-height:1}
  .brand__sub{font-size:14px;line-height:1.2}
  .card--front .brand{left:250px;top:186px}
  .card--back .brand{right:30px;top:34px}
  .card--back .brand__mark{width:44px;height:44px}
  .card--back .brand__name{font-size:36px}
  .card--back .brand__sub{font-size:12px}

  .motto{position:absolute;right:18px;top:138px;color:var(--white);font-size:14px;font-weight:500}
  .holder{position:absolute;left:40px;top:184px;color:var(--navy-deep);font-size:26px;font-weight:700}
  .contacts{position:absolute;left:40px;top:258px;list-style:none}
  .contacts li{display:flex;align-items:center;gap:16px;color:var(--white);font-size:18px;font-weight:500;height:44px}
  .contacts svg{width:28px;height:28px;flex:none}

  .partners{position:absolute;right:24px;bottom:28px;display:flex;align-items:flex-end;gap:10px}
  .partner{display:flex;align-items:center;justify-content:center;font-weight:700;color:var(--ink);height:52px;padding:0 16px;font-size:24px}
  .partner--termovo{background:var(--white)}
  .partner--ostra{background:#2a2a2a;color:var(--yellow)}
  .partner--kelm{background:var(--yellow);font-size:38px;height:74px;padding:0 22px}
</style>
</head>
<body>
<main class="sheet">

  <section class="card card--front" aria-label="Awers wizytówki">
    <svg class="shapes" viewBox="0 0 780 446" aria-hidden="true">
      <line x1="840" y1="-30" x2="590" y2="92" stroke="var(--red)" stroke-width="56"/>
      <line x1="578" y1="70" x2="540" y2="88" stroke="var(--navy)" stroke-width="4"/>
      <line x1="584" y1="82" x2="546" y2="100" stroke="var(--navy)" stroke-width="4"/>
      <line x1="590" y1="94" x2="552" y2="112" stroke="var(--navy)" stroke-width="4"/>
      <line x1="200" y1="352" x2="-60" y2="478" stroke="var(--red)" stroke-width="56"/>
      <line x1="228" y1="334" x2="266" y2="316" stroke="var(--navy)" stroke-width="4"/>
      <line x1="222" y1="322" x2="260" y2="304" stroke="var(--navy)" stroke-width="4"/>
      <line x1="216" y1="310" x2="254" y2="292" stroke="var(--navy)" stroke-width="4"/>
    </svg>
    <div class="brand">
      <span class="brand__mark"></span>
      <div>
        <div class="brand__name">Wodorex</div>
        <div class="brand__sub">Usługi Hydrauliczno-Gazowe</div>
      </div>
    </div>
  </section>

  <section class="card card--back" aria-label="Rewers wizytówki">
    <svg class="shapes" viewBox="0 0 780 446" aria-hidden="true">
      <polygon points="0,100 780,250 780,446 0,446" fill="var(--navy)"/>
      <polygon points="270,120 380,142 366,200 256,178" fill="var(--red)"/>
      <polygon points="400,128 780,128 780,166 380,166" fill="var(--red)"/>
      <polygon points="0,170 360,170 330,232 0,232" fill="var(--yellow)"/>
    </svg>

    <div class="brand">
      <span class="brand__mark"></span>
      <div>
        <div class="brand__name">Wodorex</div>
        <div class="brand__sub">Usługi Hydrauliczno-Gazowe</div>
      </div>
    </div>
    <p class="motto">...od wymiany uszczelki po wymiane łazienki.</p>

    <h1 class="holder">Marek Kowalczyk</h1>
    <ul class="contacts">
      <li>
        <svg viewBox="0 0 28 28" aria-hidden="true"><circle cx="14" cy="14" r="13" fill="var(--white)"/><path d="M10 8c1 0 2 2 2 3s-1 1-1 2 3 4 4 4 1-1 2-1 3 1 3 2-1 2-2 2c-4 0-10-6-10-10 0-1 1-2 2-2z" fill="var(--red)"/></svg>
        608 472 915
      </li>
      <li>
        <svg viewBox="0 0 28 28" aria-hidden="true"><circle cx="14" cy="14" r="13" fill="var(--white)"/><rect x="8" y="10" width="12" height="9" fill="none" stroke="var(--red)" stroke-width="1.6"/><path d="M8 10l6 5 6-5" fill="none" stroke="var(--red)" stroke-width="1.6"/></svg>
        email. info@wodorex-example.org
      </li>
      <li>
        <svg viewBox="0 0 28 28" aria-hidden="true"><circle cx="14" cy="14" r="13" fill="var(--white)"/><circle cx="14" cy="14" r="6" fill="none" stroke="var(--red)" stroke-width="1.6"/><path d="M8 14h12M14 8c-3 3-3 9 0 12M14 8c3 3 3 9 0 12" fill="none" stroke="var(--red)" stroke-width="1.4"/></svg>
        www.wodorex-example.org
      </li>
    </ul>

    <div class="partners" aria-label="Autoryzowany instalator">
      <span class="partner partner--termovo">Termovo</span>
      <span class="partner partner--ostra">Ostra</span>
      <span class="partner partner--kelm">Kelm</span>
    </div>
  </section>

</main>
</body>
</html>
```